Tarn - Stationary Design/Layout

We are a well established clothing design and manufacturing company (Tarn Sourcing) based in London UK, with our own factory in Bangladesh, supplying to many fashion retailers and brands. Our factory has very high environmental and ethical standards with people at its heart. Our quality of garments are second to none.
Our new logo has been proudly developed by the Pixel Guild community last month, we are now in the second phase and need the layout designed for our letterheads, double sided business cards, compliment slip and clothing ticket. Feel as creative as you like, but make sure it looks great!!
***The Logo - the logo design and colour is set and should NOT be changed and stay on a dark grey backround. The logo artwork to use is attached.
***Details to use for the business card:
Dorian Pelham
Direct Line: 020 7946 0158
dorian@tarnsourcing-example.com
Tarn Sourching Ltd.
57 - 59 Hollin Row
Camdon . Swindon
NW9 4QT
Switchboard: 020 7946 0274
Fax: 020 7946 0274
www.tarnsourcing-example.co.uk
***Details to use for the letterhead and compliment slip:
Tarn Sourching Ltd.
57 - 59 Hollin Row
Camdon . Swindon
NW9 4QT
Fax: 020 7946 0274
www.tarnsourcing-example.co.uk
***Details for Swing Ticket:
Size: 12cm height by 5.5cm width
One side need to have just the logo without the 'Sourcing', on the other it needs to stay blank

```html
<!DOCTYPE html>
<html lang="en">
<head>
<meta charset="utf-8">
<title>Tarn Sourcing – Stationery</title>
<link rel="stylesheet" href="https://fonts.googleapis.com/css2?family=Mulish:wght@400;700;800&display=swap">
<style>
  :root{
    --charcoal:#3a3a3a;
    --charcoal-deep:#2e2e2e;
    --amber:#f5b419;
    --silver-light:#f2f2f2;
    --silver-mid:#c9c9c9;
    --silver-dark:#9a9a9a;
    --ink:#222;
    --paper:#fff;
  }
  *{margin:0;padding:0;box-sizing:border-box}
  html,body{width:927px;height:1200px;overflow:hidden;background:var(--paper)}
  body{position:relative;font-family:"Mulish",Arial,sans-serif;color:var(--ink)}
  .abs{position:absolute}

  .brand-name{font-family:"Mulish",Arial,sans-serif;font-weight:800;color:var(--amber);letter-spacing:1px;white-space:nowrap;line-height:1}

  .sheet-corner{left:0;top:0;width:140px;height:140px}
  .sheet-brand{right:30px;top:42px;font-size:62px}

  .swing-ticket{left:38px;top:367px;width:410px;height:192px;filter:drop-shadow(2px 3px 3px rgba(0,0,0,.35))}
  .swing-ticket .brand-name{position:absolute;left:135px;top:64px;font-size:70px;letter-spacing:6px}

  .card{top:232px;width:200px;height:326px;box-shadow:2px 3px 5px rgba(0,0,0,.4);overflow:hidden}
  .card-front{left:474px;background:var(--charcoal)}
  .card-front svg{position:absolute;left:0;top:0}
  .card-front .brand-name{position:absolute;left:28px;top:48px;font-size:22px}
  .card-holder{position:absolute;left:0;width:100%;top:172px;text-align:center;font-size:12px;font-weight:700}
  .card-details{position:absolute;left:18px;top:196px;font-size:8px;line-height:10.5px}
  .card-details .gap{height:8px}
  .card-back{left:682px;background:var(--charcoal)}
  .card-back svg{position:absolute;left:0;top:0}
  .card-back .brand-name{position:absolute;left:100px;top:163px;transform:translate(-50%,-50%) rotate(90deg);font-size:54px;color:var(--silver-mid);letter-spacing:6px}

  .comp-slip{left:100px;top:576px;width:786px;height:371px;background:var(--paper);box-shadow:2px 3px 7px rgba(0,0,0,.4)}
  .comp-slip svg{position:absolute;left:0;top:0}
  .comp-slip .brand-name{position:absolute;right:28px;top:24px;font-size:56px}
  .slip-address{position:absolute;right:26px;top:284px;text-align:right;font-size:16px;font-weight:700;line-height:20px}
  .slip-greeting{position:absolute;left:18px;top:330px;font-size:26px;font-weight:700}
  .slip-greeting .accent{color:var(--amber)}

  .sheet-address{left:40px;top:1078px;font-size:16px;font-weight:700;line-height:23px}
  .sheet-address .company{font-size:20px;line-height:26px}
</style>
</head>
<body>

<svg class="abs sheet-corner" viewBox="0 0 140 140" aria-hidden="true">
  <defs>
    <linearGradient id="foldA" x1="0" y1="0" x2="1" y2="1">
      <stop offset="0" stop-color="#e6e6e6"/><stop offset="1" stop-color="#ffffff"/>
    </linearGradient>
  </defs>
  <polygon points="0,0 136,0 0,136" fill="var(--charcoal)"/>
  <polygon points="136,0 0,136 118,118" fill="url(#foldA)"/>
</svg>

<div class="abs sheet-brand brand-name">Tarn Sourcing</div>

<div class="abs swing-ticket">
  <svg width="410" height="192" viewBox="0 0 410 192" aria-hidden="true">
    <path d="M70,0 H410 V192 H70 L0,130 V62 Z" fill="var(--charcoal)"/>
    <circle cx="45" cy="90" r="16" fill="var(--paper)" stroke="#bbb" stroke-width="2"/>
    <polygon points="372,0 410,0 410,38" fill="var(--amber)"/>
    <polygon points="372,0 410,38 380,30" fill="#ddd"/>
  </svg>
  <div class="brand-name">TARN</div>
</div>

<div class="abs card card-front">
  <svg width="200" height="326" viewBox="0 0 200 326" aria-hidden="true">
    <defs>
      <linearGradient id="silverA" x1="0" y1="0" x2="1" y2="1">
        <stop offset="0" stop-color="var(--silver-dark)"/><stop offset=".5" stop-color="var(--silver-light)"/><stop offset="1" stop-color="var(--silver-mid)"/>
      </linearGradient>
    </defs>
    <path d="M0,150 C60,160 120,100 200,118 V326 H0 Z" fill="url(#silverA)"/>
  </svg>
  <div class="brand-name">Tarn Sourcing</div>
  <div class="card-holder">Dorian Pelham</div>
  <div class="card-details">
    Tarn Sourching Ltd.<br>57 - 59 Hollin Row<br>Camdon . Swindon<br>NW9 4QT
    <div class="gap"></div>
    Direct Line: 020 7946 0158<br>Switchboard: 020 7946 0274<br>Fax: 020 7946 0274<br>Email: dorian@tarnsourcing-example.com<br>Website: www.tarnsourcing-example.co.uk
  </div>
</div>

<div class="abs card card-back">
  <svg width="200" height="326" viewBox="0 0 200 326" aria-hidden="true">
    <polygon points="0,0 36,0 0,36" fill="var(--amber)"/>
    <polygon points="36,0 0,36 28,28" fill="#ddd"/>
  </svg>
  <div class="brand-name">TARN</div>
</div>

<div class="abs comp-slip">
  <svg width="90" height="90" viewBox="0 0 90 90" aria-hidden="true">
    <polygon points="0,0 82,0 0,82" fill="var(--charcoal)"/>
    <polygon points="82,0 0,82 70,70" fill="url(#foldA)"/>
  </svg>
  <div class="brand-name">Tarn Sourcing</div>
  <div class="slip-address">
    Tarn Sourching Ltd.<br>
    57 - 59 Hollin Row Camdon . Swindon NW9 4QT<br>
    Switchboard: 020 7946 0274 Fax: 020 7946 0274<br>
    Website: www.tarnsourcing-example.co.uk
  </div>
  <div class="slip-greeting"><span class="accent">With</span> Compliments</div>
</div>

<div class="abs sheet-address">
  <div class="company">Tarn Sourching Ltd.</div>
  57 - 59 Hollin Row Camdon . Swindon NW9 4QT<br>
  Switchboard: 020 7946 0274 Fax: 020 7946 0274<br>
  Website: www.tarnsourcing-example.co.uk
</div>

</body>
</html>
```